Business Card for Yachting Management Company

Need a business card design for a new yachting project management company. Attached is the logo for the company.
Our clients are large yacht owners and captains.
Design must be in the style of the logo. Modern, elegant.

Example of data to show:
Peter Hollis
Project Manager
(+34) 612 738 104
peter@quorvane.net
Quorvane Management - Meridel Tower, Office 22 - KRB - Palma de Mallorca

The data above will have to be changed (by me) for the different people in the company over the next years.

Will be printed using PrintNova (Lustre Card Series). They provide these guidelines for the size:
"the actual size of the card is 1050 x 600 pixels. However, the full bleed size is 1083 x 633 pixels, and the safe printing area is 1008 x 558 pixels."

```html
<!DOCTYPE html>
<html lang="en">
<head>
<meta charset="utf-8">
<title>Quorvane Management – Business Card</title>
<link href="https://fonts.googleapis.com/css2?family=Montserrat:wght@400;600&family=Open+Sans:wght@300&display=swap" rel="stylesheet">
<style>
  :root {
    --ink-black: #000000;
    --charcoal: #1c1c1c;
    --navy: #050538;
    --brand-blue: #0a72c0;
    --cyan: #00b8e0;
    --royal: #1a3fd0;
    --silver: #d9d9d9;
    --silver-light: #f4f4f4;
    --white: #ffffff;
  }
  * { margin: 0; padding: 0; box-sizing: border-box; }
  html, body { width: 1122px; height: 1200px; overflow: hidden; background: var(--ink-black); }
  .canvas { position: relative; width: 1122px; height: 1200px; overflow: hidden; }

  .card-front {
    position: absolute; left: 0; top: 0; width: 1122px; height: 660px;
    background: linear-gradient(135deg, var(--ink-black) 35%, #111 60%, var(--charcoal) 100%);
    overflow: hidden;
  }
  .card-front .light-bands { position: absolute; inset: 0; width: 1122px; height: 660px; }

  .pattern-area {
    position: absolute; left: 0; top: 0; width: 500px; height: 580px;
    background:
      radial-gradient(ellipse 45% 35% at 30% 20%, rgba(10,114,192,0.55), rgba(10,114,192,0) 100%),
      radial-gradient(ellipse 40% 35% at 15% 45%, rgba(217,217,217,0.35), rgba(217,217,217,0) 100%),
      radial-gradient(ellipse 40% 40% at 55% 60%, rgba(26,63,208,0.25), rgba(26,63,208,0) 100%),
      linear-gradient(160deg, #0b1a2e 0%, #050505 70%, rgba(0,0,0,0) 100%);
  }

  .identity { position: absolute; left: 550px; top: 168px; color: var(--white); font-family: "Montserrat", sans-serif; }
  .identity .person-name { font-size: 77px; font-weight: 400; line-height: 1; letter-spacing: 0.5px; }
  .identity .person-role { font-size: 30px; font-weight: 400; margin: 12px 0 0 8px; line-height: 1; }

  .contact-list { position: absolute; left: 562px; top: 345px; list-style: none; color: var(--silver-light);
    font-family: "Open Sans", sans-serif; font-weight: 300; font-size: 24px; line-height: 35px; }
  .contact-list li { display: flex; align-items: center; }
  .contact-list .icon { width: 34px; height: 34px; flex: none; margin-right: 14px; }
  .contact-list .address { margin-bottom: 24px; }
  .contact-list .phone { margin-bottom: 42px; }

  .card-back {
    position: absolute; left: 0; top: 660px; width: 1122px; height: 540px;
    background:
      radial-gradient(ellipse 75% 45% at 50% 55%, var(--ink-black) 40%, rgba(0,0,0,0) 100%),
      var(--navy);
  }
  .wordmark {
    position: absolute; left: 0; right: 0; top: 140px; text-align: center;
    font-family: "Montserrat", sans-serif; font-weight: 600; color: var(--brand-blue); line-height: 1;
  }
  .wordmark .wordmark-name { display: block; font-size: 132px; letter-spacing: 2px; }
  .wordmark .wordmark-sub { display: block; font-size: 46px; letter-spacing: 22px; margin-top: 40px; padding-left: 22px; }
</style>
</head>
<body>
<main class="canvas">
  <section class="card-front">
    <svg class="light-bands" viewBox="0 0 1122 660" aria-hidden="true">
      <polygon points="330,660 1122,0 1122,120 480,660" fill="#ffffff" opacity="0.025"/>
      <polygon points="600,660 1122,230 1122,320 760,660" fill="#ffffff" opacity="0.04"/>
      <polygon points="0,533 1122,533 1122,660 0,660" fill="#ffffff" opacity="0.015"/>
    </svg>

    <div class="pattern-area" role="img" aria-label="Decorative pattern of overlapping blue and silver diamond shapes"></div>

    <header class="identity">
      <h1 class="person-name">Peter Hollis</h1>
      <p class="person-role">Project Manager</p>
    </header>

    <ul class="contact-list">
      <li class="address">
        <svg class="icon" viewBox="0 0 34 34" aria-hidden="true">
          <path d="M17 4 C11 4 7 8.5 7 14 C7 20 17 30 17 30 C17 30 27 20 27 14 C27 8.5 23 4 17 4 Z M17 10 A4 4 0 1 1 16.99 10 Z" fill="var(--white)" fill-rule="evenodd"/>
        </svg>
        <span>Quorvane Management - Meridel Tower,<br>Office 22 - KRB - Palma de Mallorca</span>
      </li>
      <li class="phone">
        <svg class="icon" viewBox="0 0 34 34" aria-hidden="true">
          <path d="M8 3 L13 3 L15 11 L11.5 13.5 C13 18 16 21 20.5 22.5 L23 19 L31 21 L31 26 C31 28.5 29 31 26 31 C15 30 4 19 3 8 C3 5 5.5 3 8 3 Z" fill="var(--white)"/>
        </svg>
        <span>(+34) 612 738 104</span>
      </li>
      <li class="web">
        <svg class="icon" viewBox="0 0 34 34" aria-hidden="true">
          <g fill="none" stroke="var(--white)" stroke-width="2">
            <circle cx="17" cy="17" r="15"/>
            <ellipse cx="17" cy="17" rx="7" ry="15"/>
            <line x1="17" y1="2" x2="17" y2="32"/>
            <line x1="2" y1="17" x2="32" y2="17"/>
            <path d="M5 9 H29 M5 25 H29"/>
          </g>
        </svg>
        <span>peter@quorvane.net</span>
      </li>
    </ul>
  </section>

  <section class="card-back">
    <div class="wordmark">
      <span class="wordmark-name">Quorvane</span>
      <span class="wordmark-sub">MANAGEMENT</span>
    </div>
  </section>
</main>
</body>
</html>
```